Create website design - Leashline

Build website to specification. Look and feel only or include all functionality. I have put together a google document which includes all information on requirements. I will share this with you via message once you have been assigned the job.

Coding

Coded - Design and coding required

Number of Pages Required

1 page

Requirements
Must have
• As per Google Doc
Nice to have
• As per Google Doc
Should not have
• As per Google Doc

```html
<!DOCTYPE html>
<html lang="en">
<head>
<meta charset="utf-8">
<title>Leashline – Pet Sitters &amp; Dog Walkers</title>
<link href="https://fonts.googleapis.com/css2?family=Playfair+Display:wght@400;500;600&family=Montserrat:wght@300;400;500;600;700&display=swap" rel="stylesheet">
<style>
:root{
  --blue:#2c7cd0;
  --blue-dark:#2168b5;
  --ink:#2f3a48;
  --heading:#4b5563;
  --muted:#8a929c;
  --text:#59616b;
  --pale:#eef3fb;
  --line:#e6ebf2;
  --footer:#2e2f31;
  --footer-text:#c9ccd1;
  --white:#ffffff;
}
*{box-sizing:border-box;margin:0;padding:0}
html,body{width:1200px;height:5300px;overflow:hidden}
body{position:relative;font-family:'Montserrat',sans-serif;color:var(--text);background:var(--white)}
.abs{position:absolute}
.serif{font-family:'Playfair Display',serif}
a{color:inherit;text-decoration:none}

/* header */
.topbar{left:453px;top:0;width:747px;height:52px;background:var(--blue);clip-path:polygon(18px 0,100% 0,100% 100%,0 100%)}
.topbar ul{display:flex;list-style:none;height:52px;align-items:center;padding-left:42px}
.topbar li{color:var(--white);font-size:14px;margin-right:51px}
.brand{left:128px;top:62px;font-size:32px;font-weight:600;color:var(--blue)}
.brand::before{content:"";position:absolute;left:-2px;top:-22px;width:24px;height:24px;border-radius:50%;border:2px solid var(--blue)}
.mainnav{left:435px;top:84px;display:flex;list-style:none}
.mainnav li{font-size:15px;font-weight:500;color:var(--ink);margin-right:45px}

/* hero */
.hero{left:0;top:130px;width:1200px;height:576px;background:linear-gradient(100deg,#6f6a66 0%,#9a8470 35%,#c99b6b 55%,#b5aea6 75%,#d9dad6 100%)}
.hero-title{left:0;top:322px;width:1200px;text-align:center;color:var(--white);font-size:46px;line-height:46px;font-weight:500;text-shadow:0 2px 6px rgba(0,0,0,.35)}
.search{left:319px;top:451px;width:562px;height:58px;background:var(--white);border-radius:8px;box-shadow:0 0 0 3px rgba(255,255,255,.5)}
.search span{position:absolute;left:40px;top:19px;font-size:14px;color:#9aa1a9}
.search .pin{position:absolute;left:14px;top:18px}
.search .go{position:absolute;right:6px;top:6px;width:46px;height:46px;border-radius:7px;background:var(--blue)}
.search .go svg{margin:12px}

/* services */
.band-pale{left:0;width:1200px;background:var(--pale)}
.eyebrow{left:0;top:764px;width:1200px;text-align:center;color:var(--blue);font-size:23px}
.sec-title{left:0;width:1200px;text-align:center;color:var(--heading);font-size:42px;line-height:50px;font-weight:500}
.services{left:128px;top:932px;width:946px;height:539px;background:var(--white);border-radius:34px;box-shadow:0 4px 24px rgba(40,70,110,.08);display:grid;grid-template-columns:repeat(3,1fr);grid-template-rows:1fr 1fr}
.svc{text-align:center;padding-top:42px;border-right:1px solid var(--line);border-bottom:1px solid var(--line)}
.svc:nth-child(3n){border-right:none}
.svc:nth-child(n+4){border-bottom:none}
.svc svg{width:68px;height:62px}
.svc h3{font-size:19px;color:var(--blue);font-weight:600;margin-top:16px;margin-bottom:8px}
.svc p{font-size:14.5px;line-height:21px;color:var(--text);width:240px;margin:0 auto}

/* about */
.about-title{left:128px;top:1626px;width:424px;text-align:right;font-size:42px;color:var(--heading);font-weight:500}
.about-text{left:128px;top:1700px;width:432px;text-align:right;font-size:15.5px;line-height:24px;color:var(--text)}
.btn{left:395px;top:1949px;width:161px;height:48px;border-radius:24px;background:var(--blue);color:var(--white);font-size:15px;font-weight:700;text-align:center;line-height:48px}
.about-photo{left:603px;top:1582px;width:597px;height:476px;border-radius:28px 0 0 28px;background:linear-gradient(120deg,#e9c58d 0%,#d8a86c 40%,#a98a66 70%,#7e8c9c 100%)}

/* customers */
.review{width:294px;height:268px;top:2397px;background:var(--white);border-radius:10px;box-shadow:0 4px 20px rgba(40,70,110,.1);text-align:center;padding-top:84px}
.avatar{width:96px;height:96px;border-radius:50%;top:2355px;border:3px solid var(--white)}
.review h4{font-family:'Playfair Display',serif;color:var(--blue);font-size:18px;font-weight:600}
.review .when{font-size:14px;color:#a5acb4;margin-top:2px}
.review p{font-size:14.5px;line-height:21px;font-style:italic;color:var(--text);width:250px;margin:17px auto 0}

/* video */
.video{left:0;top:2789px;width:1200px;height:476px;background:linear-gradient(180deg,#b9c58f 0%,#8c9a5a 40%,#7c8a45 70%,#b44a4a 100%)}
.play{left:559px;top:2994px;width:82px;height:82px;border-radius:50%;border:4px solid var(--white);background:rgba(0,0,0,.25)}

/* how */
.step-ring{width:154px;height:154px;border-radius:50%;border:3px solid #8a97a6;background:var(--pale)}
.step-num{font-size:88px;color:var(--blue);font-weight:300;line-height:88px;font-family:'Montserrat',sans-serif}
.step-title{width:330px;text-align:center;font-size:25px;font-weight:400;color:var(--ink)}
.step-text{width:280px;text-align:center;font-size:14.5px;line-height:18px;color:var(--muted)}
.connector{height:2px;background:#8a97a6;top:3505px}
.dot{width:12px;height:12px;border-radius:50%;background:var(--blue);top:3500px}

/* blog */
.post{top:3986px;width:290px;height:383px;background:var(--white);box-shadow:0 4px 20px rgba(40,70,110,.1);text-align:center}
.post .ph{height:192px}
.post h4{font-size:18px;line-height:20px;color:var(--ink);font-weight:600;margin:40px auto 0;width:230px}
.post p{font-size:14px;line-height:17px;color:var(--muted);margin:12px auto 0;width:236px}
.post .date{font-size:15px;font-weight:700;color:var(--blue);margin-top:14px}

/* newsletter + footer */
.footer{left:0;top:4651px;width:1200px;height:649px;background:var(--footer)}
.news{left:128px;top:4493px;width:942px;height:319px;background:var(--blue);border-radius:8px;text-align:center;color:var(--white)}
.news h2{font-size:35px;font-weight:500;margin-top:88px}
.news p{font-size:14.5px;margin-top:6px}
.news .field{position:absolute;left:119px;top:191px;width:605px;height:52px;background:var(--white);border-radius:4px 0 0 4px;text-align:left;padding:17px;font-size:14px;color:#a5acb4}
.news .signup{position:absolute;left:724px;top:191px;width:119px;height:52px;background:#2a2b2d;border-radius:0 4px 4px 0;font-size:15px;font-weight:700;line-height:52px}
.f-brand{left:128px;top:4922px;font-size:32px;font-weight:600;color:var(--blue)}
.f-brand::before{content:"";position:absolute;left:-2px;top:-22px;width:24px;height:24px;border-radius:50%;border:2px solid var(--blue)}
.f-about{left:128px;top:5002px;width:262px;font-size:14.5px;line-height:24.5px;color:var(--footer-text)}
.f-col h5{font-family:'Playfair Display',serif;font-size:29px;color:var(--white);font-weight:500}
.f-col ul{list-style:none;margin-top:24px}
.f-col li{font-size:14.5px;color:var(--footer-text);height:31px}
.contact li{display:flex;gap:10px;height:auto;margin-bottom:14px;line-height:18px}
.contact svg{flex:none;margin-top:2px}
.f-rule{left:128px;top:5217px;width:944px;height:1px;background:#47484b}
.copy{left:0;top:5254px;width:1200px;text-align:center;font-size:14.5px;color:var(--footer-text)}
</style>
</head>
<body>

<header>
  <nav class="abs topbar"><ul><li>Find a Sitter</li><li>Become a Sitter</li><li>Help Centre</li><li>Sign up</li><li>Log in</li></ul></nav>
  <a class="abs brand">Leashline</a>
  <ul class="abs mainnav"><li>Pet Services</li><li>Pet Health</li><li>Pet Insurance</li><li>Pet Products</li><li>Contact</li></ul>
</header>

<section>
  <div class="abs hero" role="img" aria-label="Photo of a woman relaxing on a sofa with her dog in a bright living room"></div>
  <h1 class="abs hero-title serif">Find trusted, local Pet<br>Sitters &amp; Dog Walkers</h1>
  <div class="abs search">
    <svg class="pin" width="16" height="22" viewBox="0 0 16 22"><path d="M8 1a7 7 0 0 0-7 7c0 5 7 13 7 13s7-8 7-13a7 7 0 0 0-7-7z" fill="#3a4350"/><circle cx="8" cy="8" r="2.6" fill="#fff"/></svg>
    <span>Enter Location Type</span>
    <div class="go"><svg width="22" height="22" viewBox="0 0 22 22"><circle cx="9" cy="9" r="6" fill="none" stroke="#fff" stroke-width="3"/><path d="M13.5 13.5l6 6" stroke="#fff" stroke-width="3" stroke-linecap="round"/></svg></div>
  </div>
</section>

<section>
  <div class="abs band-pale" style="top:1309px;height:858px"></div>
  <p class="abs eyebrow serif">Pet Services</p>
  <h2 class="abs sec-title serif" style="top:804px">Australia’s largest online<br>pet care marketplace</h2>
  <div class="abs services">
    <div class="svc">
      <svg viewBox="0 0 68 62" fill="none" stroke="#2c7cd0" stroke-width="2.5" stroke-linejoin="round"><path d="M8 28L34 6l26 22"/><path d="M14 24v32h40V24"/><circle cx="34" cy="42" r="6"/><circle cx="26" cy="33" r="3"/><circle cx="34" cy="30" r="3"/><circle cx="42" cy="33" r="3"/></svg>
      <h3>Pet Hosting</h3><p>Lorem ipsum dolor sit amet consectetur adipiscing elit sed do eiusmod tempor inc.</p>
    </div>
    <div class="svc">
      <svg viewBox="0 0 68 62" fill="none" stroke="#2c7cd0" stroke-width="2.5" stroke-linejoin="round"><path d="M8 28L34 6l26 22"/><path d="M14 24v32h40V24"/><path d="M28 54V38l6-6 6 6v16"/></svg>
      <h3>Pet sitting</h3><p>Lorem ipsum dolor sit amet consectetur adipiscing elit sed do eiusmod tempor inc.</p>
    </div>
    <div class="svc">
      <svg viewBox="0 0 68 62" fill="none" stroke="#2c7cd0" stroke-width="2.5" stroke-linejoin="round"><path d="M34 56S8 40 8 22a12 12 0 0 1 26-6 12 12 0 0 1 26 6c0 18-26 34-26 34z"/><circle cx="34" cy="32" r="5"/><circle cx="26" cy="24" r="2.5"/><circle cx="34" cy="21" r="2.5"/><circle cx="42" cy="24" r="2.5"/></svg>
      <h3>Pet day care</h3><p>Lorem ipsum dolor sit amet consectetur adipiscing elit sed do eiusmod tempor inc.</p>
    </div>
    <div class="svc">
      <svg viewBox="0 0 68 62" fill="none" stroke="#2c7cd0" stroke-width="2.5" stroke-linejoin="round"><path d="M6 28L34 6l28 22"/><path d="M12 24v32h44V24"/><path d="M24 56V40a10 10 0 0 1 20 0v16"/><path d="M24 30h20"/></svg>
      <h3>House visiting</h3><p>Lorem ipsum dolor sit amet consectetur adipiscing elit sed do eiusmod tempor inc.</p>
    </div>
    <div class="svc">
      <svg viewBox="0 0 68 62" fill="none" stroke="#2c7cd0" stroke-width="2.5" stroke-linecap="round"><circle cx="48" cy="8" r="5"/><path d="M48 14v20l-6 20M48 34l6 20M48 20l-10 10"/><path d="M38 30L20 40"/><rect x="8" y="40" width="16" height="8" rx="3"/><path d="M10 48v8M22 48v8"/></svg>
      <h3>Dog walking</h3><p>Lorem ipsum dolor sit amet consectetur adipiscing elit sed do eiusmod tempor inc.</p>
    </div>
    <div class="svc">
      <svg viewBox="0 0 68 62" fill="none" stroke="#2c7cd0" stroke-width="2.5" stroke-linecap="round"><path d="M54 6l-10 10M58 18l-8 0M46 4l0 8"/><path d="M16 30h22v12H16z"/><path d="M18 42v12M36 42v12M38 30l6-8"/></svg>
      <h3>Dog training</h3><p>Lorem ipsum dolor sit amet consectetur adipiscing elit sed do eiusmod tempor inc.</p>
    </div>
  </div>

  <h2 class="abs about-title serif">About Us</h2>
  <p class="abs about-text">Sed ut perspiciatis unde omnis iste natus error sit voluptatem accusantium doloremque laudantium, totam rem aperiam, eaque ipsa quae ab illo inve lorentore veritatis et quasi architecto beatae vitae dicta sunt explicabo. Nemo enim ipsam volup tate lormquia voluptas sit aspernatur aut odit aut fugit, loresed quia consequuntur magni dolores eos qui ratione voluptatem sequi nesciunt. Neque porro qu is quam est, qui dolorem ipsum quia dolo.</p>
  <a class="abs btn">READ MORE</a>
  <div class="abs about-photo" role="img" aria-label="Photo of a smiling woman hugging a golden labrador outdoors"></div>
</section>

<section>
  <h2 class="abs sec-title serif" style="top:2270px">Happy Customers.</h2>
  <div class="abs review" style="left:128px"><h4>Mara Whitfield</h4><div class="when">1 month ago</div><p>Lorem ipsum dolor sit amet, consectetur adipiscing elit se do eiusmod tempor incididut labore et dolore magn.</p></div>
  <div class="abs review" style="left:453px"><h4>Mara Whitfield</h4><div class="when">1 month ago</div><p>Lorem ipsum dolor sit amet, consectetur adipiscing elit se do eiusmod tempor incididut labore et dolore magn.</p></div>
  <div class="abs review" style="left:780px"><h4>Mara Whitfield</h4><div class="when">1 month ago</div><p>Lorem ipsum dolor sit amet, consectetur adipiscing elit se do eiusmod tempor incididut labore et dolore magn.</p></div>
  <div class="abs avatar" style="left:227px;background:linear-gradient(135deg,#c48a55,#6b4a33)" role="img" aria-label="Customer photo with a dog"></div>
  <div class="abs avatar" style="left:552px;background:linear-gradient(135deg,#9fae86,#b2533f)" role="img" aria-label="Customer photo with a dog in a park"></div>
  <div class="abs avatar" style="left:879px;background:linear-gradient(135deg,#d8d2c8,#7c6452)" role="img" aria-label="Customer photo at home with a pet"></div>
</section>

<section>
  <div class="abs video" role="img" aria-label="Video still of a family lying on a picnic blanket in the grass with their golden retriever"></div>
  <div class="abs play"><svg width="74" height="74" viewBox="0 0 74 74"><path d="M30 24v26l20-13z" fill="#fff"/></svg></div>
</section>

<section>
  <div class="abs band-pale" style="top:3265px;height:553px"></div>
  <h2 class="abs sec-title serif" style="top:3322px">How Does it Work?</h2>

  <div class="abs connector" style="left:331px;width:132px"></div>
  <div class="abs dot" style="left:457px"></div>
  <div class="abs connector" style="left:675px;width:132px"></div>
  <div class="abs dot" style="left:801px"></div>

  <div class="abs step-ring" style="left:176px;top:3428px"></div>
  <div class="abs step-num" style="left:160px;top:3460px">1</div>
  <svg class="abs" style="left:222px;top:3478px" width="62" height="62" viewBox="0 0 62 62" fill="none" stroke="#2c7cd0" stroke-width="2.5"><circle cx="26" cy="26" r="18"/><path d="M39 39l16 16" stroke-linecap="round"/><circle cx="26" cy="30" r="5"/><circle cx="19" cy="22" r="2.5"/><circle cx="26" cy="19" r="2.5"/><circle cx="33" cy="22" r="2.5"/></svg>
  <h3 class="abs step-title serif" style="left:88px;top:3600px">Search for a Sitter</h3>
  <p class="abs step-text" style="left:123px;top:3662px">Lorem ipsum dolor sit amet, cons ectetur adipiscing elit, sed do eius mod tempor incididunt</p>

  <div class="abs step-ring" style="left:520px;top:3428px"></div>
  <div class="abs step-num" style="left:502px;top:3460px">2</div>
  <svg class="abs" style="left:578px;top:3482px" width="56" height="56" viewBox="0 0 56 56" fill="none" stroke="#2c7cd0" stroke-width="2.5"><rect x="4" y="8" width="40" height="36" rx="3"/><path d="M4 18h40M14 4v8M34 4v8"/><path d="M12 26h6M22 26h6M12 34h6"/><circle cx="40" cy="42" r="10" fill="#eef3fb"/><path d="M40 36v6l4 3"/></svg>
  <h3 class="abs step-title serif" style="left:432px;top:3602px">Make a booking</h3>
  <p class="abs step-text" style="left:462px;top:3662px">Lorem ipsum dolor sit amet, cons ectetur adipiscing elit, sed do eius mod tempor incididunt</p>

  <div class="abs step-ring" style="left:860px;top:3428px"></div>
  <div class="abs step-num" style="left:838px;top:3460px">3</div>
  <svg class="abs" style="left:912px;top:3478px" width="60" height="60" viewBox="0 0 60 60" fill="none" stroke="#2c7cd0" stroke-width="2.5"><circle cx="24" cy="16" r="9"/><path d="M8 54V40a16 16 0 0 1 32 0v14"/><rect x="38" y="34" width="14" height="10" rx="3"/><path d="M40 44v8M50 44v8"/></svg>
  <h3 class="abs step-title serif" style="left:781px;top:3596px">Enjoy peace of mind</h3>
  <p class="abs step-text" style="left:805px;top:3662px">Lorem ipsum dolor sit amet, cons ectetur adipiscing elit, sed do eius mod tempor incididunt</p>
</section>

<section>
  <h2 class="abs sec-title serif" style="top:3878px">Latest Blog Posts</h2>
  <article class="abs post" style="left:128px"><div class="ph" style="background:linear-gradient(135deg,#d9c7ad,#b07a4a)" role="img" aria-label="Photo of a woman playing with a dog on the beach"></div><h4>Lorem ipsum dolor sit am etconse ctetore.</h4><p>Lorem ipsum dolor sit ametco nectetur adipiscing elit, sedod olor eiusmod tempor.</p><div class="date">July 27 2023</div></article>
  <article class="abs post" style="left:455px"><div class="ph" style="background:linear-gradient(135deg,#8ea27a,#5c6b47)" role="img" aria-label="Photo of a dog walker with several dogs in a park"></div><h4>Lorem ipsum dolor sit am etconse ctetore.</h4><p>Lorem ipsum dolor sit ametco nectetur adipiscing elit, sedod olor eiusmod tempor.</p><div class="date">July 27 2023</div></article>
  <article class="abs post" style="left:782px"><div class="ph" style="background:linear-gradient(135deg,#a9c08a,#4f6a3c)" role="img" aria-label="Photo of a woman on a park bench with her dog"></div><h4>Lorem ipsum dolor sit am etconse ctetore.</h4><p>Lorem ipsum dolor sit ametco nectetur adipiscing elit, sedod olor eiusmod tempor.</p><div class="date">July 27 2023</div></article>
</section>

<footer>
  <div class="abs footer"></div>
  <div class="abs news">
    <h2 class="serif">Be the first to get notified of new opportunities</h2>
    <p>Lorem ipsum dolor sit amet, consectetur adipiscing elit, sed do eiusmod temp.</p>
    <div class="field">Email:</div>
    <div class="signup">SIGN UP</div>
  </div>

  <a class="abs f-brand">Leashline</a>
  <p class="abs f-about">Lorem ipsum dolor sit amet, consectetur adipiscing elit, sed do eiusmod tempor incididunt ut labore et dolore magna aliqua. Quis ipsum suspendisse ultrices gravidus commodia.</p>

  <div class="abs f-col" style="left:461px;top:4892px"><h5>Explore</h5><ul><li>About Us</li><li>Our Blog</li><li>Press</li><li>Jobs</li><li>Reviews</li><li>Investor Centre</li><li>Sustainability</li></ul></div>
  <div class="abs f-col" style="left:677px;top:4892px"><h5>Links</h5><ul><li>At Sitter's Home</li><li>Dog Walking</li><li>At Pet's Home</li><li>Pet Day Care</li><li>Dog Sitting</li><li>House Visiting</li><li>Cat Sitting</li></ul></div>
  <div class="abs f-col contact" style="left:864px;top:4892px"><h5>Contact</h5>
    <ul>
      <li><svg width="12" height="16" viewBox="0 0 12 16"><path d="M6 0a6 6 0 0 0-6 6c0 4 6 10 6 10s6-6 6-10a6 6 0 0 0-6-6z" fill="#fff"/><circle cx="6" cy="6" r="2" fill="#2e2f31"/></svg><span>Lorem Vale road 48 KPT<br>dumy numers 217.</span></li>
      <li><svg width="14" height="14" viewBox="0 0 14 14"><path d="M3 0l3 3-2 2a8 8 0 0 0 5 5l2-2 3 3-2 3C6 14 0 8 0 3z" fill="#fff"/></svg><span>Phone: 55 010 2468</span></li>
      <li><svg width="14" height="11" viewBox="0 0 14 11"><rect width="14" height="11" rx="1" fill="#fff"/><path d="M0 1l7 5 7-5" stroke="#2e2f31" fill="none"/></svg><span>Email:hello@leashline.example</span></li>
    </ul>
  </div>
  <div class="abs f-rule"></div>
  <p class="abs copy">Copyright © 2023 &nbsp;All Rights Reserved.</p>
</footer>

</body>
</html>
```